Bref créative
Harbor Crest card design
biz card
Bright & Fun-filled
Dennis Pollard
Senior Healthcare Specialist
P.O. Box 42916
Asheville, NC 28492
dpollard4@velmora.net
please include my picture on the business card. I will attach it in the upload section.
please add the info that I currently have on the back of my business card now. I will upload that as well.
Front of Current Business Card
Back of Current Business Card
Headshot for Card
new logo to use for card front

```html
<!DOCTYPE html>
<html lang="en">
<head>
<meta charset="UTF-8">
<title>Harbor Crest Inc – Business Card</title>
<link href="https://fonts.googleapis.com/css2?family=Open+Sans:wght@400;600;700&display=swap" rel="stylesheet">
<style>
  :root {
    --page-bg: #e9e4dc;
    --card-bg: #ffffff;
    --brand-blue: #1f5d95;
    --deep-blue: #1a5289;
    --accent-orange: #f58220;
    --text-dark: #2b2b2b;
    --photo-top: #7d8a99;
    --photo-bottom: #2c3443;
  }
  * { box-sizing: border-box; margin: 0; padding: 0; }
  html, body {
    width: 1200px; height: 780px; overflow: hidden;
    background: var(--page-bg);
    font-family: "Open Sans", Arial, sans-serif;
  }
  .business-card {
    position: absolute; left: 50px; top: 75px;
    width: 1100px; height: 630px;
    background: var(--card-bg);
    border-radius: 26px;
    overflow: hidden;
    box-shadow: 0 6px 18px rgba(0,0,0,0.18);
  }
  .card-swoosh { position: absolute; inset: 0; width: 100%; height: 100%; }
  .brand {
    position: absolute; left: 44px; top: 150px;
    display: flex; align-items: center; gap: 14px;
  }
  .brand-dot {
    width: 22px; height: 22px; border-radius: 50%;
    background: var(--brand-blue);
  }
  .brand-name {
    font-size: 46px; font-weight: 700; letter-spacing: 1px;
    color: var(--brand-blue); text-transform: uppercase;
  }
  .mailing-address {
    position: absolute; left: 46px; top: 300px;
    font-size: 22px; line-height: 30px; color: var(--text-dark);
  }
  .contact-list {
    position: absolute; left: 46px; top: 410px;
    list-style: none; font-size: 21px; line-height: 33px; color: var(--text-dark);
  }
  .contact-list li { display: flex; align-items: center; gap: 12px; }
  .contact-list svg { width: 20px; height: 20px; fill: var(--brand-blue); flex: none; }
  .headshot {
    position: absolute; left: 695px; top: 95px;
    width: 205px; height: 250px; border-radius: 10px;
    background: linear-gradient(180deg, var(--photo-top), var(--photo-bottom));
  }
  .specialist {
    position: absolute; left: 640px; top: 360px; width: 315px;
    text-align: center;
  }
  .specialist-name { font-size: 30px; font-weight: 700; color: var(--deep-blue); }
  .specialist-title { font-size: 20px; font-weight: 700; color: var(--accent-orange); }
</style>
</head>
<body>
  <section class="business-card">
    <svg class="card-swoosh" viewBox="0 0 1100 630" preserveAspectRatio="none" aria-hidden="true">
      <path d="M0 630 L0 585 Q560 610 1100 455 L1100 630 Z" fill="var(--brand-blue)"/>
      <path d="M0 560 Q560 595 1100 425" fill="none" stroke="var(--accent-orange)" stroke-width="14"/>
    </svg>

    <div class="brand">
      <span class="brand-dot"></span>
      <span class="brand-name">Harbor Crest Inc</span>
    </div>

    <address class="mailing-address" style="font-style:normal">
      P.O. Box 42916<br>
      Asheville, NC 28492
    </address>

    <ul class="contact-list">
      <li>
        <svg viewBox="0 0 24 24"><path d="M6.6 10.8a15 15 0 0 0 6.6 6.6l2.2-2.2c.3-.3.7-.4 1-.2 1.1.4 2.3.6 3.6.6.6 0 1 .4 1 1V20c0 .6-.4 1-1 1A17 17 0 0 1 3 4c0-.6.4-1 1-1h3.5c.6 0 1 .4 1 1 0 1.3.2 2.5.6 3.6.1.3 0 .7-.2 1z"/></svg>
        828-407-3362
      </li>
      <li>
        <svg viewBox="0 0 24 24"><path d="M7 1h10a2 2 0 0 1 2 2v18a2 2 0 0 1-2 2H7a2 2 0 0 1-2-2V3a2 2 0 0 1 2-2zm0 4v13h10V5zm5 14.5a1.2 1.2 0 1 0 0 2.4 1.2 1.2 0 0 0 0-2.4z"/></svg>
        828-619-2854
      </li>
      <li>
        <svg viewBox="0 0 24 24"><path d="M2 5h20v14H2zm2 2v.5l8 5 8-5V7zm0 2.8V17h16V9.8l-8 5z"/></svg>
        dpollard4@velmora.net
      </li>
    </ul>

    <div class="headshot" role="img" aria-label="Headshot photo of Dennis Pollard"></div>

    <div class="specialist">
      <div class="specialist-name">Dennis Pollard</div>
      <div class="specialist-title">Senior Healthcare Specialist</div>
    </div>
  </section>
</body>
</html>
```